TechNurse Atlantic
TechNurse Atlantic - Computers
Creative Brief
Professional
Derwin Halcott Jr., MCP
Partner
47 Marlow Lane Hamilton HM11, Suite 208 Bermuda
dhalcott@wirelunabda.com
http://www.wirelunabda.com
Please note that #21 is the winning logo for TechNurse. Please design stationary based on this, thanks. http://orders.brandquillhub.com/contests/technurse-atlantic

```html
<!DOCTYPE html>
<html lang="en">
<head>
<meta charset="utf-8">
<title>TechNurse Atlantic – Stationery</title>
<link rel="stylesheet" href="https://fonts.googleapis.com/css2?family=Open+Sans:wght@400;600;800&display=swap">
<style>
:root{
  --stage:#3b3b3d;
  --paper:#ffffff;
  --red:#b3121b;
  --red-dark:#6e0a0f;
  --ink:#2b2b2b;
  --grey:#8a8a8a;
  --ghost:#e9e9ea;
  --shadow:rgba(0,0,0,.45);
}
*{box-sizing:border-box;margin:0;padding:0}
html,body{width:1200px;height:722px;overflow:hidden;background:var(--stage);font-family:"Open Sans",Arial,sans-serif;color:var(--ink)}
.stage{position:relative;width:1200px;height:722px;background:radial-gradient(ellipse at 50% 40%,#4a4a4c 0%,var(--stage) 70%)}
.piece{position:absolute;background:var(--paper);overflow:hidden;box-shadow:0 4px 12px var(--shadow)}
.swoosh{position:absolute;left:0;bottom:0;width:100%}
.brand{display:flex;align-items:center;gap:6px;font-weight:800;color:var(--red);letter-spacing:.5px}
.brand-mark{background:var(--red);display:block}
.ghost-brand{position:absolute;font-weight:800;color:var(--ghost);white-space:nowrap;letter-spacing:2px}
.contact{font-size:5.5px;line-height:1.55;color:var(--ink)}
.contact b{color:var(--red);font-weight:600;display:inline-block;width:22px}
.contact .company{color:var(--red);font-weight:600}

/* letterhead */
.letterhead{left:173px;top:29px;width:446px;height:650px}
.letterhead .brand{position:absolute;left:26px;top:22px;font-size:21px}
.letterhead .brand-mark{width:14px;height:14px}
.letterhead .contact{position:absolute;left:283px;top:22px}
.letterhead .ghost-brand{right:22px;bottom:118px;font-size:46px}
.letterhead .swoosh{height:110px}

/* business cards */
.card{left:43px;width:305px;height:185px;border-radius:6px}
.card-front{top:223px}
.card-front .brand{position:absolute;left:16px;top:40px;font-size:16px}
.card-front .brand-mark{width:11px;height:11px}
.card-front .person{position:absolute;left:142px;top:24px}
.person-name{font-size:11px;font-weight:600;color:var(--red)}
.person-role{font-size:6px;color:var(--grey);margin-bottom:14px}
.card-front .swoosh{height:48px}
.card-back{top:451px}
.card-back .ghost-brand{left:8px;top:52px;font-size:44px}
.card-back .brand{position:absolute;right:30px;top:44px;font-size:17px}
.card-back .brand-mark{width:12px;height:12px}
.card-back .web{position:absolute;right:30px;top:96px;font-size:7.5px;font-weight:600;color:var(--ink)}
.card-back .swoosh{height:48px}

/* envelope */
.envelope{left:643px;top:29px;width:516px;height:264px}
.envelope .flap{position:absolute;left:0;top:0;width:100%;height:150px}
.envelope .brand{position:absolute;left:50%;top:18px;transform:translateX(-50%);font-size:18px}
.envelope .brand-mark{width:12px;height:12px}

/* compliment slip */
.slip{left:643px;top:365px;width:516px;height:321px}
.slip .brand{position:absolute;left:26px;top:24px;font-size:21px}
.slip .brand-mark{width:14px;height:14px}
.slip .contact{position:absolute;left:26px;top:96px}
.slip .ghost-brand{left:180px;top:150px;font-size:48px}
.slip .swoosh{height:78px}
</style>
</head>
<body>
<main class="stage">

  <svg width="0" height="0" style="position:absolute">
    <defs>
      <linearGradient id="band-red" x1="0" y1="0" x2="1" y2="0">
        <stop offset="0" stop-color="#6e0a0f"/>
        <stop offset=".5" stop-color="#c8161f"/>
        <stop offset="1" stop-color="#7a0b10"/>
      </linearGradient>
      <symbol id="wave" viewBox="0 0 400 100" preserveAspectRatio="none">
        <path d="M0 55 C110 20 230 95 400 40 L400 100 L0 100 Z" fill="#d9d9db"/>
        <path d="M0 68 C120 35 240 100 400 52 L400 100 L0 100 Z" fill="url(#band-red)"/>
        <path d="M0 84 C130 60 250 105 400 75 L400 100 L0 100 Z" fill="#5a080c"/>
        <path d="M0 68 C120 35 240 100 400 52" fill="none" stroke="#ffffff" stroke-width="1.2" opacity=".7"/>
      </symbol>
    </defs>
  </svg>

  <section class="piece letterhead" aria-label="Letterhead">
    <div class="brand"><span class="brand-mark"></span>TechNurse</div>
    <div class="contact">
      <div class="company">TechNurse</div>
      47 Marlow Lane Hamilton HM11, Suite 208<br>Bermuda<br>
      <b>Phone:</b>(441) 555-0142<br>
      <b>Email:</b>dhalcott@wirelunabda.com<br>
      <b>Web:</b>http://www.wirelunabda.com
    </div>
    <div class="ghost-brand">TechNurse</div>
    <svg class="swoosh"><use href="#wave"/></svg>
  </section>

  <section class="piece card card-front" aria-label="Business card front">
    <div class="brand"><span class="brand-mark"></span>TechNurse</div>
    <div class="person">
      <div class="person-name">Derwin Halcott Jr., MCP</div>
      <div class="person-role">Partner</div>
      <div class="contact">
        47 Marlow Lane Hamilton HM11, Suite 208<br>Bermuda<br>
        <b>Phone:</b>(441) 555-0142<br>
        <b>Cell:</b>(441) 555-0187<br>
        <b>Email:</b>dhalcott@wirelunabda.com<br>
        <b>Web:</b>http://www.wirelunabda.com
      </div>
    </div>
    <svg class="swoosh"><use href="#wave"/></svg>
  </section>

  <section class="piece card card-back" aria-label="Business card back">
    <div class="ghost-brand">TechNurse</div>
    <div class="brand"><span class="brand-mark"></span>TechNurse</div>
    <div class="web">www.wirelunabda.com</div>
    <svg class="swoosh"><use href="#wave"/></svg>
  </section>

  <section class="piece envelope" aria-label="Envelope">
    <svg class="flap" viewBox="0 0 516 150" preserveAspectRatio="none">
      <path d="M0 0 L258 150 L516 0" fill="none" stroke="#dcdcdc" stroke-width="1.5"/>
    </svg>
    <div class="brand"><span class="brand-mark"></span>TechNurse</div>
  </section>

  <section class="piece slip" aria-label="Compliment slip">
    <div class="brand"><span class="brand-mark"></span>TechNurse</div>
    <div class="contact">
      <div class="company">TechNurse</div>
      47 Marlow Lane Hamilton HM11, Suite 208<br>Bermuda<br>
      <b>Phone:</b>(441) 555-0142<br>
      <b>Email:</b>dhalcott@wirelunabda.com<br>
      <b>Web:</b>http://www.wirelunabda.com
    </div>
    <div class="ghost-brand">TechNurse</div>
    <svg class="swoosh"><use href="#wave"/></svg>
  </section>

</main>
</body>
</html>
```